現在ホームページリニューアルを検討しております。
社内でのデザインだとどうしても前情報がある分、発想の限界、偏りがどうしてもあります。

今回はなるべくフラットな状態でデザインを検討したいと考えておりますので、こちらで公募をさせていただくことにしました。

既存の歯科医院のデザインやイメージに縛られることなく、自由な発想でご提案頂きたいと思っております。

■依頼内容

PC・スマートフォン用 それぞれ1枚 合計2枚
(実装する際にはレスポンシブの予定です。)

診療科目は
小児
一般
矯正(大学から月に数回先生にお越し頂いています)

医院の特徴
ショッピングモール内にあります
駐車場あり
バリアフリー
お子さんの遊びスペースあり
デザイナー物件

ページ数
2ページ
希望イメージ
シンプル 複雑
単色 カラフル
暗い 明るい
日常 高級
遊び心 厳粛
未来的 伝統的
女性的 男性的
納品ファイル
• 高解像度JPG (.jpg)
• フォトショップ形式 (.psd)
• PNG形式 (.png)
▼弊社が用意するもの
・ページ構成
・テキスト
・ワイヤーフレーム
・ロゴ
・写真
※受注者様のご意向があれば、ビデオ通話などで対応することも可能です。
※ページ構成や画像などは、個別に送らせていただきたいので、まずはご提案またはメッセージにてご連絡ください。

▼依頼の流れ
1.ご提案
ご提案をいただき次第、弊社よりTOPページの構成をお送りします。
3.デザイン作成
デザインを作成しましたら、提案の【追記する】からデザインファイルの追加をしてください。
5.修正依頼
修正していただきたい箇所がある場合は、修正依頼をいたしますので、修正案を再提案してください。
6.納品
フォトショップ(psd)またはイラストレーター(ai)形式で納品をしていただきます。納品が完了次第、当選を行います。

弊社では、複数のWEBサイトを運用しております。
今回はTOPページのみの依頼となっておりますが、継続的に依頼をさせていただくことも考えております。
ご提案をお待ちしております。
ワイヤーフレームと写真素材を添付します。
依頼金額を45000円に変更して、延長しました。
たくさんのご応募ありがとうございます。
現在、選考中です。3~7日程度で当選デザインを決定できるかと思いますので、今しばらくお待ちください。

歯科医院スタッフの投票にて決定いたしました。

たくさんのご提案ありがとうございます。また機会があれば、是非よろしくお願いいたします。

```html
<!DOCTYPE html>
<html lang="ja">
<head>
<meta charset="utf-8">
<title>〇〇歯科医院</title>
<link rel="stylesheet" href="https://fonts.googleapis.com/css2?family=Noto+Sans+JP:wght@400;500;700&family=Roboto:wght@400;700&display=swap">
<style>
:root{
  --blue:#1f6fd1;
  --blue-dark:#1559ad;
  --blue-light:#e4effc;
  --blue-pale:#f2f7fd;
  --text:#333;
  --muted:#777;
  --line:#d6e3f3;
  --white:#fff;
}
*{margin:0;padding:0;box-sizing:border-box}
html,body{width:1200px;height:3732px;overflow:hidden}
body{font-family:"Noto Sans JP",sans-serif;color:var(--text);background:var(--white);position:relative}
section,header,footer{position:absolute;left:0;width:1200px}

/* header */
.site-header{top:0;height:132px;background:var(--white)}
.brand{position:absolute;left:60px;top:28px}
.brand small{display:block;font-size:12px;color:var(--muted);letter-spacing:.1em}
.brand strong{display:block;font-size:34px;font-weight:700;color:var(--blue);line-height:1.2}
.hours{position:absolute;left:430px;top:6px;border-collapse:collapse;font-size:10px;text-align:center}
.hours th,.hours td{border:1px solid var(--line);width:34px;height:22px}
.hours th{background:var(--blue);color:var(--white);font-weight:500}
.hours td:first-child,.hours th:first-child{width:86px}
.hours td{color:var(--blue)}
.header-contact{position:absolute;right:60px;top:8px;width:300px}
.tel{display:flex;align-items:center;gap:8px;font-family:"Roboto",sans-serif;font-weight:700;font-size:34px;color:var(--blue);line-height:1.2}
.tel svg{flex:none}
.btn{display:flex;align-items:center;justify-content:center;gap:10px;background:var(--blue);color:var(--white);font-size:14px;font-weight:500;border-radius:4px}
.header-contact .btn{height:40px;margin-top:10px}

/* hero */
.hero{top:132px;height:468px}
.hero-photo{position:absolute;inset:0;background:linear-gradient(100deg,#f2f1ee 0%,#e7e4dd 45%,#d9d4c8 70%,#ece9e3 100%)}
.hero-copy{position:absolute;left:130px;top:90px;font-size:50px;font-weight:700;color:var(--blue);line-height:1.3}
.hero-copy span{display:inline-block;background:rgba(255,255,255,.9);padding:0 10px;margin-bottom:6px}
.hero .btn{position:absolute;left:130px;top:340px;width:270px;height:56px;font-size:16px}

/* treatments */
.treatments{top:660px;height:900px}
.card{position:absolute;width:272px;height:270px}
.card-photo{height:110px;background:linear-gradient(135deg,#dfe9f6,#f4e5df)}
.card-body{background:var(--blue-pale);height:160px;padding:14px 16px}
.card h3{font-size:15px;font-weight:700;color:var(--blue);margin-bottom:8px}
.card p{font-size:11px;line-height:1.8;color:var(--muted)}

/* headings */
.sec-title{text-align:center}
.sec-title h2{font-family:"Roboto",sans-serif;font-size:38px;font-weight:700;color:var(--blue);line-height:1.1}
.sec-title p{font-size:12px;color:var(--muted);margin-top:4px}

/* concept */
.concept{top:1625px;height:530px;background:var(--blue-light)}
.concept .sec-title{margin-top:30px}
.concept-item{position:absolute;top:150px;width:300px;text-align:center}
.concept-photo{width:280px;height:280px;border-radius:50%;margin:0 auto;border:6px solid var(--white);background:linear-gradient(135deg,#f3e3d8,#cfe0f2)}
.concept-item p{font-size:17px;font-weight:700;color:var(--blue);margin-top:16px;line-height:1.5}

/* information */
.information{top:2180px;height:470px}
.news{position:absolute;left:360px;top:100px;width:580px;list-style:none}
.news li{display:flex;height:28px;align-items:center;font-size:12px;padding-left:16px;border-bottom:1px solid var(--white)}
.news li:nth-child(odd){background:var(--blue-light)}
.news time{width:130px;color:var(--blue);font-family:"Roboto",sans-serif}
.information .btn{position:absolute;left:480px;top:390px;width:240px;height:46px}

/* greeting */
.greeting{top:2720px;height:340px}
.greeting-photo{position:absolute;inset:0;background:linear-gradient(180deg,#ebe7e0,#f7f5f1 60%,#e9e4da)}
.greeting .sec-title{position:relative;margin-top:36px}
.greeting-text{position:absolute;left:200px;top:130px;width:800px;font-size:13px;line-height:2.1;color:#444}

/* access */
.access{top:3060px;height:300px;background:var(--blue-light)}
.map{position:absolute;left:130px;top:20px;width:460px;height:260px;background:linear-gradient(135deg,#eef0ee,#dfe6e9)}
.access-info{position:absolute;left:630px;top:18px;width:440px}
.access-info small{display:block;font-size:11px;color:var(--muted);line-height:1.4}
.access-info strong{display:block;font-size:30px;color:var(--blue);line-height:1.2}
.access-info address{font-style:normal;font-size:11px;color:var(--muted);margin:2px 0 4px;line-height:1.6}
.access-info .tel{font-size:28px}
.access-info .hours{position:static;margin-top:6px;background:var(--white)}
.access-info .btn{width:280px;height:40px;margin-top:10px}

/* footer */
.site-footer{top:3390px;height:342px}
.footer-col{position:absolute;top:10px;width:200px;font-size:12px}
.footer-col h4{font-size:13px;font-weight:700;margin-bottom:12px}
.footer-col ul{list-style:none;color:var(--muted);line-height:2.3}
.copyright{position:absolute;left:0;bottom:0;width:1200px;height:32px;background:var(--blue);color:var(--white);font-size:11px;text-align:center;line-height:32px}
</style>
</head>
<body>

<header class="site-header">
  <div class="brand"><small>CHILDREN &amp; FAMILY DENTAL</small><strong>〇〇歯科医院</strong></div>
  <table class="hours">
    <tr><th>診療時間</th><th>月</th><th>火</th><th>水</th><th>木</th><th>金</th><th>土</th><th>日</th></tr>
    <tr><td>9:30〜13:00</td><td>●</td><td>●</td><td>●</td><td>●</td><td>●</td><td>●</td><td>―</td></tr>
    <tr><td>14:30〜19:00</td><td>●</td><td>●</td><td>●</td><td>●</td><td>●</td><td>▲</td><td>―</td></tr>
  </table>
  <div class="header-contact">
    <div class="tel"><svg width="30" height="30" viewBox="0 0 24 24"><rect width="24" height="24" rx="4" fill="#1f6fd1"/><path d="M8 5l2 3-1.5 1.5a9 9 0 006 6L16 14l3 2-1 3c-6 0-12-6-12-12z" fill="#fff"/></svg>03-9876-5432</div>
    <div class="btn"><svg width="16" height="16" viewBox="0 0 16 16"><rect x="1" y="3" width="14" height="12" rx="1" fill="none" stroke="#fff" stroke-width="1.5"/><path d="M1 7h14" stroke="#fff" stroke-width="1.5"/></svg>WEBからのご予約はこちら</div>
  </div>
</header>

<section class="hero">
  <div class="hero-photo" role="img" aria-label="白を基調とした明るい院内の待合室の写真"></div>
  <h1 class="hero-copy"><span>お子様連れでも</span><br><span>安心の</span><br><span>託児サービス</span></h1>
  <div class="btn">治療シミュレーション <svg width="12" height="12" viewBox="0 0 12 12"><path d="M4 2l4 4-4 4" stroke="#fff" stroke-width="2" fill="none"/></svg></div>
</section>

<section class="treatments">
  <article class="card" style="left:132px;top:0"><div class="card-photo" role="img" aria-label="歯の模型の写真"></div><div class="card-body"><h3>治療名</h3><p>治療内容の説明が入ります。治療内容の説明が入ります。治療内容の説明が入ります。治療内容の説明が入ります。</p></div></article>
  <article class="card" style="left:464px;top:0"><div class="card-photo" role="img" aria-label="笑顔の女性スタッフの写真"></div><div class="card-body"><h3>治療名</h3><p>治療内容の説明が入ります。治療内容の説明が入ります。治療内容の説明が入ります。治療内容の説明が入ります。</p></div></article>
  <article class="card" style="left:796px;top:0"><div class="card-photo" role="img" aria-label="インプラント模型の写真"></div><div class="card-body"><h3>治療名</h3><p>治療内容の説明が入ります。治療内容の説明が入ります。治療内容の説明が入ります。治療内容の説明が入ります。</p></div></article>
  <article class="card" style="left:132px;top:310px"><div class="card-photo" role="img" aria-label="診療中の歯科医師の写真"></div><div class="card-body"><h3>治療名</h3><p>治療内容の説明が入ります。治療内容の説明が入ります。治療内容の説明が入ります。治療内容の説明が入ります。</p></div></article>
  <article class="card" style="left:464px;top:310px"><div class="card-photo" role="img" aria-label="子どもと母親の写真"></div><div class="card-body"><h3>治療名</h3><p>治療内容の説明が入ります。治療内容の説明が入ります。治療内容の説明が入ります。治療内容の説明が入ります。</p></div></article>
  <article class="card" style="left:796px;top:310px"><div class="card-photo" role="img" aria-label="歯の治療の様子の写真"></div><div class="card-body"><h3>治療名</h3><p>治療内容の説明が入ります。治療内容の説明が入ります。治療内容の説明が入ります。治療内容の説明が入ります。</p></div></article>
  <article class="card" style="left:132px;top:620px"><div class="card-photo" role="img" aria-label="診察を受ける患者の写真"></div><div class="card-body"><h3>治療名</h3><p>治療内容の説明が入ります。治療内容の説明が入ります。治療内容の説明が入ります。治療内容の説明が入ります。</p></div></article>
  <article class="card" style="left:464px;top:620px"><div class="card-photo" role="img" aria-label="子どもの歯科検診の写真"></div><div class="card-body"><h3>治療名</h3><p>治療内容の説明が入ります。治療内容の説明が入ります。治療内容の説明が入ります。治療内容の説明が入ります。</p></div></article>
  <article class="card" style="left:796px;top:620px"><div class="card-photo" role="img" aria-label="歯の断面図のイラスト"></div><div class="card-body"><h3>治療名</h3><p>治療内容の説明が入ります。治療内容の説明が入ります。治療内容の説明が入ります。治療内容の説明が入ります。</p></div></article>
</section>

<section class="concept">
  <div class="sec-title"><h2>Concept</h2><p>コンセプト</p></div>
  <div class="concept-item" style="left:130px"><div class="concept-photo" role="img" aria-label="歯みがきをする子どもたちの写真"></div><p>痛くない歯科治療</p></div>
  <div class="concept-item" style="left:450px;top:125px"><div class="concept-photo" role="img" aria-label="キッズスペースで遊ぶ親子の写真"></div><p>お子様連れでも<br>安心の託児所</p></div>
  <div class="concept-item" style="left:770px"><div class="concept-photo" role="img" aria-label="歯科医師とスタッフの写真"></div><p>何度も通院させない<br>歯医者</p></div>
</section>

<section class="information">
  <div class="sec-title"><h2>Information</h2><p>お知らせ</p></div>
  <ul class="news">
    <li><time>2020.02.10</time>ここにタイトルが入ります</li>
    <li><time>2020.02.08</time>ここにタイトルが入ります</li>
    <li><time>2020.02.05</time>ここにタイトルが入ります</li>
    <li><time>2020.02.01</time>ここにタイトルが入ります</li>
    <li><time>2020.01.28</time>ここにタイトルが入ります</li>
    <li><time>2020.01.24</time>ここにタイトルが入ります</li>
    <li><time>2020.01.20</time>ここにタイトルが入ります</li>
    <li><time>2020.01.15</time>ここにタイトルが入ります</li>
    <li><time>2020.01.10</time>ここにタイトルが入ります</li>
  </ul>
  <div class="btn">一覧を見る <svg width="12" height="12" viewBox="0 0 12 12"><path d="M4 2l4 4-4 4" stroke="#fff" stroke-width="2" fill="none"/></svg></div>
</section>

<section class="greeting">
  <div class="greeting-photo" role="img" aria-label="ぼかした院内の写真"></div>
  <div class="sec-title"><h2>Greeting</h2><p>ご挨拶</p></div>
  <p class="greeting-text">この文章は院長挨拶のダミーテキストです。この文章は院長挨拶のダミーテキストです。この文章は院長挨拶のダミーテキストです。この文章は院長挨拶のダミーテキストです。この文章は院長挨拶のダミーテキストです。この文章は院長挨拶のダミーテキストです。<br><br>この文章は院長挨拶のダミーテキストです。この文章は院長挨拶のダミーテキストです。この文章は院長挨拶のダミーテキストです。この文章は院長挨拶のダミーテキストです。この文章は院長挨拶のダミーテキストです。この文章は院長挨拶のダミーテキストです。</p>
</section>

<section class="access">
  <div class="map" role="img" aria-label="医院周辺の地図"></div>
  <div class="access-info">
    <small>CHILDREN &amp; FAMILY DENTAL</small>
    <strong>〇〇歯科医院</strong>
    <address>〒000-0000 東京都青葉区みどり町1-2-3 モール2F<br>駐車場あり・バリアフリー対応</address>
    <div class="tel"><svg width="28" height="28" viewBox="0 0 24 24"><rect width="24" height="24" rx="4" fill="#1f6fd1"/><path d="M8 5l2 3-1.5 1.5a9 9 0 006 6L16 14l3 2-1 3c-6 0-12-6-12-12z" fill="#fff"/></svg>03-9876-5432</div>
    <table class="hours">
      <tr><th>診療時間</th><th>月</th><th>火</th><th>水</th><th>木</th><th>金</th><th>土</th><th>日</th></tr>
      <tr><td>9:30〜13:00</td><td>●</td><td>●</td><td>●</td><td>●</td><td>●</td><td>●</td><td>―</td></tr>
      <tr><td>14:30〜19:00</td><td>●</td><td>●</td><td>●</td><td>●</td><td>●</td><td>▲</td><td>―</td></tr>
    </table>
    <div class="btn">WEBからのご予約はこちら</div>
  </div>
</section>

<footer class="site-footer">
  <div class="footer-col" style="left:130px"><h4>医院のコンセプト</h4><ul><li>痛くない歯科治療</li><li>お子様連れでも安心の託児所</li><li>何度も通院させない歯医者</li></ul></div>
  <div class="footer-col" style="left:360px"><h4>診療科目</h4><ul><li>小児歯科</li><li>一般歯科</li><li>矯正歯科</li></ul></div>
  <div class="footer-col" style="left:600px"><ul><li>医院案内</li><li>スタッフ紹介</li><li>設備紹介</li><li>料金表</li></ul></div>
  <div class="footer-col" style="left:840px"><ul><li>お知らせ</li><li>アクセス</li><li>よくある質問</li><li>採用情報</li><li>プライバシーポリシー</li></ul></div>
  <div class="copyright">© 〇〇歯科医院 All Rights Reserved.</div>
</footer>

</body>
</html>
```